New iOS App design for Boston Startup

We are looking for a new app design for our iPhone app. The current app's design feels outdated and we like to add lots of new functionality and a new navigation as well. A complete overhaul therefore!
We want you to design 5 screens that will have changed the most. The complete wireframes of these 5 pages are attached in the requirements document.
Once the winning design is selected we will award the winner with the designing all other screens (40-50 screens based on the same design). This will be a separate project worth $1000. The winning designer can get more follow up work if both sides are happy about the cooperation.
We will give feedback as soon as the first screen has been uploaded for review. Final decision will be made only after all 5 screens are finished.
We hope you give it your best!
Note: will only communicate through ArtVantle (no skype),
Updates
Reason: Want to give designers a chance to submit their designs as I understand from some, the deadline is too close.
I have raised the award and introduced a 2nd price as well to make it worth your time. I hope you give it your best shot.
Reason: A few of you have asked for an extension of the deadline as time is running out. I will extend by one day. Tell me if you need more.
Industry/Entity Type
Startup
Requirements
Must have
- At least 1 screen before we can give you feedback.
Nice to have
- multiple options of 1 screen to get to a desirable design

```html
<!DOCTYPE html>
<html lang="en">
<head>
<meta charset="utf-8">
<title>Home – Study App</title>
<link rel="stylesheet" href="https://fonts.googleapis.com/css2?family=Open+Sans:wght@400;600;700&display=swap">
<style>
:root{
  --bg:#eeeeec;
  --teal:#0f9a7e;
  --teal-light:#6cc8b4;
  --purple:#c64ef0;
  --purple-frame:#b84fe6;
  --gauge-grey:#a6a6a6;
  --band:#cfcfcf;
  --band-line:#b3b3b3;
  --tab:#8c8c8c;
  --ink:#1b1b1b;
  --muted:#555555;
  --up:#3ca33c;
  --white:#ffffff;
  --black:#000000;
}
*{box-sizing:border-box;margin:0;padding:0}
html,body{width:676px;height:1200px;overflow:hidden;background:var(--bg)}
body{font-family:"Open Sans",Arial,sans-serif;color:var(--ink);position:relative}
.frame{position:absolute;left:0;top:0;width:676px;height:1200px;overflow:hidden}
.screen{position:absolute;left:0;top:0;width:640px;height:1136px;overflow:hidden;transform:scale(1.05625);transform-origin:0 0;
  background:radial-gradient(circle at 40% 30%,#f6f6f4 0%,var(--bg) 70%)}
.abs{position:absolute}
.status-bar{left:0;top:0;width:640px;height:40px;background:var(--black);color:var(--white);font-size:22px;font-weight:600}
.status-bar .carrier{left:52px;top:5px;white-space:nowrap}
.status-bar .time{left:0;width:640px;text-align:center;top:5px}
.menu-button{left:24px;top:70px;width:45px;height:34px}
.menu-button span{display:block;height:7px;background:#9a9a9a;border-radius:2px;margin-bottom:7px}
.greeting{left:30px;width:610px;top:60px;text-align:center;color:var(--teal);font-size:33px;font-weight:700;letter-spacing:2px;white-space:nowrap}
.avatar{left:24px;top:183px;width:96px;height:93px;border:4px solid var(--purple-frame);background:linear-gradient(160deg,#8c7a6e,#c9a894 55%,#4d4a48)}
.user-name{left:0;width:172px;top:287px;text-align:center;font-size:18px;font-weight:700;letter-spacing:1px;white-space:nowrap}
.gauge{left:0;top:0}
.score-label{left:275px;width:200px;top:343px;text-align:center;font-size:21px;font-weight:700;letter-spacing:2px;line-height:31px}
.stats-band{left:0;top:428px;width:640px;height:124px;background:linear-gradient(#d8d8d8,var(--band))}
.stat-divider{top:0;width:2px;height:124px;background:var(--band-line)}
.stat-value{top:26px;font-size:28px;color:var(--ink);white-space:nowrap;display:flex;align-items:center}
.stat-value svg{margin:0 2px}
.stat-caption{top:76px;font-size:26px;color:var(--muted);white-space:nowrap}
.nav-list{left:70px;top:581px;width:500px}
.nav-item{position:relative;height:80px;background:var(--purple);color:var(--white);font-size:25px;display:flex;align-items:center;padding-left:32px;margin-bottom:2px}
.nav-item svg{position:absolute;right:22px;top:26px}
.next-lesson{left:70px;top:853px}
.next-lesson-text{left:70px;width:460px;top:888px;text-align:center;color:var(--white);line-height:1.2;white-space:nowrap}
.next-lesson-text .topic{font-size:22px}
.next-lesson-text .lesson{font-size:29px}
.tab{top:1041px;width:92px;height:80px;background:var(--tab);color:var(--white);font-size:18px;text-align:center;border:1px solid #7a7a7a}
.tab svg{display:block;margin:6px auto 0}
.tab span{display:block;margin-top:2px}
.tab.is-active{top:1021px;height:100px;width:113px;background:var(--white);color:var(--purple);border:2px solid #9a9a9a}
</style>
</head>
<body>
<div class="frame">
<div class="screen">
  <div class="abs status-bar">
    <svg class="abs" style="left:8px;top:12px" width="42" height="18"><g fill="#fff"><rect x="0" y="12" width="6" height="5"/><rect x="8" y="9" width="6" height="8"/><rect x="16" y="6" width="6" height="11"/><rect x="24" y="3" width="6" height="14"/><rect x="32" y="0" width="6" height="17"/></g></svg>
    <div class="abs carrier">ORBIT&nbsp;&nbsp; 3G</div>
    <div class="abs time">9:51 PM</div>
    <svg class="abs" style="left:557px;top:9px" width="20" height="20"><circle cx="10" cy="10" r="9" fill="#fff"/><path d="M10 4v6h4" stroke="#000" stroke-width="2" fill="none"/></svg>
    <svg class="abs" style="left:590px;top:10px" width="44" height="20"><rect x="1" y="1" width="38" height="18" rx="3" fill="none" stroke="#fff" stroke-width="2"/><rect x="4" y="4" width="32" height="12" fill="#fff"/><rect x="40" y="6" width="3" height="8" fill="#fff"/></svg>
  </div>

  <div class="abs menu-button"><span></span><span></span><span></span></div>
  <h1 class="abs greeting">Welcome back, Noam!</h1>

  <div class="abs avatar" role="img" aria-label="Profile photo of the user"></div>
  <div class="abs user-name">Noam Keller</div>

  <svg class="abs gauge" width="640" height="420" aria-label="Score gauge">
    <defs><clipPath id="score-disc"><circle cx="375" cy="272" r="65"/></clipPath></defs>
    <path d="M282 348 A118 118 0 0 1 461 194.5" fill="none" stroke="var(--teal)" stroke-width="24"/>
    <path d="M461 194.5 A118 118 0 0 1 461 355" fill="none" stroke="var(--gauge-grey)" stroke-width="24"/>
    <g clip-path="url(#score-disc)">
      <rect x="300" y="200" width="150" height="150" fill="var(--teal-light)"/>
      <ellipse cx="375" cy="330" rx="110" ry="82" fill="var(--teal)"/>
    </g>
    <text x="375" y="276" text-anchor="middle" font-family="Open Sans,sans-serif" font-size="34" font-weight="700" fill="#111" letter-spacing="2">640</text>
    <path d="M351 289v16M344 299l7 7 7-7" fill="none" stroke="#111" stroke-width="2.5"/>
    <text x="364" y="307" font-family="Open Sans,sans-serif" font-size="19" font-weight="700" fill="#111">-18</text>
  </svg>
  <div class="abs score-label">YOUR<br>SCORE!</div>

  <div class="abs stats-band">
    <svg class="abs" style="left:0;top:46px" width="16" height="28"><path d="M2 2l10 12L2 26" fill="none" stroke="#fff" stroke-width="4"/></svg>
    <div class="abs stat-value" style="left:64px">34%<svg width="18" height="28"><path d="M9 1L1 12h5v15h6V12h5z" fill="var(--up)" stroke="#2a7a2a"/></svg>&nbsp;+4</div>
    <div class="abs stat-caption" style="left:57px">Completion</div>
    <div class="abs stat-divider" style="left:227px"></div>
    <div class="abs stat-value" style="left:240px">20<svg width="18" height="28"><path d="M9 1L1 12h5v15h6V12h5z" fill="var(--up)" stroke="#2a7a2a"/></svg>+3</div>
    <div class="abs stat-caption" style="left:258px">Sessions</div>
    <div class="abs stat-value" style="left:370px">18<svg width="18" height="28"><path d="M9 1L1 12h5v15h6V12h5z" fill="var(--up)" stroke="#2a7a2a"/></svg>+10</div>
    <div class="abs stat-caption" style="left:390px">Min.</div>
    <div class="abs stat-divider" style="left:496px"></div>
    <div class="abs stat-caption" style="left:511px">This week</div>
    <svg class="abs" style="left:622px;top:46px" width="18" height="28"><path d="M16 2L6 14l10 12" fill="none" stroke="#fff" stroke-width="4"/></svg>
  </div>

  <nav class="abs nav-list">
    <div class="nav-item">Analytics<svg width="26" height="28"><path d="M4 2l14 12L4 26" fill="none" stroke="#fff" stroke-width="6"/></svg></div>
    <div class="nav-item">Course Overview<svg width="26" height="28"><path d="M4 2l14 12L4 26" fill="none" stroke="#fff" stroke-width="6"/></svg></div>
    <div class="nav-item" style="height:76px">Days until test 33<svg width="26" height="28"><path d="M4 2l14 12L4 26" fill="none" stroke="#fff" stroke-width="6"/></svg></div>
  </nav>

  <svg class="abs next-lesson" width="504" height="128"><path d="M0 20H425V0L502 64 425 127V108H0Z" fill="var(--teal)"/></svg>
  <div class="abs next-lesson-text"><div class="topic">Up Next: Sentence Correction</div><div class="lesson">Lesson 4</div></div>

  <div class="abs tab" style="left:43px"><svg width="60" height="44"><path d="M30 8C22 2 10 2 4 5v33c6-3 18-3 26 3 8-6 20-6 26-3V5C50 2 38 2 30 8zM30 8v33" fill="none" stroke="#fff" stroke-width="3"/></svg><span>Theory</span></div>
  <div class="abs tab" style="left:152px"><svg width="50" height="44"><rect x="3" y="3" width="44" height="38" fill="none" stroke="#fff" stroke-width="3"/><g fill="#fff"><rect x="8" y="10" width="34" height="2"/><rect x="8" y="21" width="34" height="2"/><rect x="8" y="32" width="34" height="2"/></g></svg><span>Practice</span></div>
  <div class="abs tab is-active" style="left:265px"><svg width="54" height="46"><path d="M27 4L3 24h7v20h13V31h8v13h13V24h7z" fill="var(--purple)"/></svg><span>Home</span></div>
  <div class="abs tab" style="left:400px"><svg width="46" height="46"><rect x="2" y="2" width="42" height="42" rx="6" fill="#fff"/><g fill="#555"><circle cx="12" cy="12" r="4"/><circle cx="34" cy="12" r="4"/><circle cx="23" cy="23" r="4"/><circle cx="12" cy="34" r="4"/><circle cx="34" cy="34" r="4"/></g></svg><span>Games</span></div>
  <div class="abs tab" style="left:511px"><svg width="50" height="46"><rect x="3" y="8" width="36" height="36" fill="#fff"/><path d="M10 24l10 10L46 4" fill="none" stroke="#333" stroke-width="6"/></svg><span>Test</span></div>
</div>
</div>
</body>
</html>
```